Professional law firm looking for new professional and eye-catching business card design

Law firm in need of new business card design using existing firm logo and firm colors on thick card stock. Firm colors are navy blue, cyan blue, and gray. Please use firm's logo either on the back of the card or on the front and back. I am looking for something eye-catching and resonating but also professional.

Target Market(s)

Law firm growth by attracting clients with professional, creative, and attractive business cards.

Industry/Entity Type

Legal/Law Firm

Contact Information for Business Card

Name: Derek T. Halloway, Esq., Address: 517 E. Quintley Blvd., P.O. Box 641, Tavares, FL 32790, Phone numbers: (352) 555-0187 Office, (352) 555-0142 Fax, email address: DerekH@hqlegalfx.com, website: www.HQLegalFX.com

Font styles to use
Other font styles liked:
• Font as close as possible to matching law firm logo.

Requirements
Must have
• Must have business card details and law firm logo with law firm colors.

```html
<!DOCTYPE html>
<html lang="en">
<head>
<meta charset="utf-8">
<title>HQ Legal – Business Card</title>
<link rel="stylesheet" href="https://fonts.googleapis.com/css2?family=Cormorant+SC:wght@500;600&display=swap">
<style>
  :root {
    --stage: #0c0c0c;
    --navy: #141d27;
    --charcoal: #1c1c21;
    --cyan: #1ba3db;
    --gray: #a9aab0;
    --ink: #e6e7ea;
  }
  * { margin: 0; padding: 0; box-sizing: border-box; }
  html, body {
    width: 1200px; height: 792px; overflow: hidden;
    background: var(--stage);
    font-family: "Cormorant SC", Georgia, serif;
  }
  .stage { position: relative; width: 1200px; height: 792px; }
  .card { position: absolute; overflow: hidden; }
  .card--front { left: 97px; top: 243px; width: 485px; height: 261px; background: var(--navy); }
  .card--back { left: 638px; top: 243px; width: 482px; height: 257px; background: var(--charcoal); }

  .mark-dot { position: absolute; border-radius: 50%; background: var(--gray); opacity: .85; }
  .firm-name { position: absolute; color: var(--cyan); font-weight: 600; line-height: 1; white-space: nowrap; }
  .firm-sub { position: absolute; color: var(--cyan); font-weight: 600; line-height: 1; white-space: nowrap; }
  .firm-rule { position: absolute; height: 2px; background: var(--gray); }

  .card--front .mark-dot { left: 74px; top: 120px; width: 22px; height: 22px; }
  .card--front .firm-name { left: 104px; top: 120px; font-size: 19px; }
  .card--front .firm-sub { left: 104px; top: 144px; font-size: 9px; }

  .contact { position: absolute; left: 272px; top: 78px; color: var(--ink); font-weight: 600; }
  .contact__name { font-size: 13.5px; letter-spacing: .3px; margin-bottom: 11px; }
  .contact__line { display: flex; align-items: center; gap: 6px; font-size: 9.5px; height: 14px; }
  .contact__line svg { width: 9px; height: 9px; fill: var(--cyan); flex: none; }
  .contact__address { margin-top: 13px; font-size: 9.5px; line-height: 11.5px; }

  .card--back .mark-dot { left: 170px; top: 112px; width: 30px; height: 30px; }
  .card--back .firm-name { left: 210px; top: 108px; font-size: 30px; }
  .card--back .firm-rule { left: 210px; top: 148px; width: 118px; }
  .card--back .firm-sub { left: 210px; top: 156px; font-size: 11px; }
  .website { position: absolute; left: 0; right: 0; top: 222px; text-align: center; color: var(--ink); font-size: 9.5px; font-weight: 600; }
</style>
</head>
<body>
<main class="stage">
  <section class="card card--front" aria-label="Card front">
    <span class="mark-dot" aria-hidden="true"></span>
    <div class="firm-name">HQ Legal</div>
    <div class="firm-sub">Halloway &amp; Quint, P.A.</div>

    <div class="contact">
      <p class="contact__name">Derek T. Halloway, Esq.</p>
      <p class="contact__line">
        <svg viewBox="0 0 10 10" aria-hidden="true"><path d="M0 2h10v6H0z" fill="none" stroke="#1ba3db" stroke-width="1"/><path d="M0 2l5 3.5L10 2" fill="none" stroke="#1ba3db" stroke-width="1"/></svg>
        DerekH@hqlegalfx.com
      </p>
      <p class="contact__line">
        <svg viewBox="0 0 10 10" aria-hidden="true"><path d="M2 0.5l2 2-1 1.2c.6 1.3 1.6 2.3 2.9 2.9L7 5.6l2.5 2L8.3 9.5C4.2 9.3.7 5.8.5 1.7z"/></svg>
        (352) 555-0187
      </p>
      <p class="contact__line">
        <svg viewBox="0 0 10 10" aria-hidden="true"><rect x="2.5" y="0.5" width="5" height="3"/><rect x="0.5" y="3.5" width="9" height="4.5" rx="1"/><rect x="2.5" y="7" width="5" height="2.5"/></svg>
        (352) 555-0142
      </p>
      <p class="contact__address">517 E. Quintley Blvd.,<br>P.O. Box 641, Tavares,<br>FL 32790</p>
    </div>
  </section>

  <section class="card card--back" aria-label="Card back">
    <span class="mark-dot" aria-hidden="true"></span>
    <div class="firm-name">HQ Legal</div>
    <div class="firm-rule"></div>
    <div class="firm-sub">Halloway &amp; Quint, P.A.</div>
    <p class="website">www.HQLegalFX.com</p>
  </section>
</main>
</body>
</html>
```